Mexican Themed Party Invitations!

Hi,
We are wanting a Mexican themed party invititation for Derek's 40th!
We are wanting something that resembles an old Mexican postcard – like the ones you used to get in the 50’s–70's - the size would approximately be 7" by 5.5".
We would preferably like a double sided invite - The below details would be displayed on the back somewhere:
If there could also be room left somewhere on the back to attach a small magnet so that the invite can be stuck on the fridge:)
Derek's 40th
When: Saturday the 27th of July 2013 @ 7PM
Where: 48 Farrow Terrace, Coromandel Valley, SA
Bring: Yourself and cowboy drinkin’ boots
RSVP: Date, email and phone – make funny RSVP email address!
Dress: Preferably traditional Mexican or 70’s Cowboy/Girl – but tacky Sombrero’s and Ponchos are OK too!
Men: There will be a prize for the best grown (real) Mexican moustache
Music: by the Dusty Spurs, Mexican Mariachi Band
Food: Supplied by……
Drinks: Bartender Neville will have the tequila shots and sangria ready to go
RSVP: by the 1st of July
Please note that we have attached some examples of pictures that we like as a bit of inspiration to give you a bit of an idea of which direction we are wanting to go in.
70's style would be good as Derek was born then.
We can't wait to see what you come up with!!!
Updates
Just for some inspration I found this image, which I love! If someone could do something like this, that would be awesome!
http://www.bids.pebblecart.com/stuff/k/k_chh_tolova_greet_57260.jpg
Paco's 40th insted of Tolova (or similar)

```html
<!DOCTYPE html>
<html lang="en">
<head>
<meta charset="utf-8">
<title>Paco's 40th – Greetings from Mexico</title>
<link rel="stylesheet" href="https://fonts.googleapis.com/css2?family=Alfa+Slab+One&family=Bowlby+One&family=Yellowtail&family=Allura&family=Abril+Fatface&display=swap">
<style>
  :root {
    --paper: #f3e2b3;
    --paper-edge: #e8d49f;
    --sepia-light: #a9a489;
    --sepia-mid: #7d7a63;
    --sepia-dark: #45443a;
    --chili: #e8341b;
    --cream: #fbf6e2;
    --ink: #1f211d;
  }
  html, body {
    margin: 0;
    padding: 0;
    width: 1200px;
    height: 857px;
    overflow: hidden;
    background: var(--paper);
  }
  .postcard {
    position: relative;
    width: 1200px;
    height: 857px;
    background: var(--paper);
  }
  .postcard__photo {
    position: absolute;
    left: 28px;
    top: 32px;
    width: 1144px;
    height: 796px;
    background:
      radial-gradient(ellipse at 62% 30%, rgba(210,205,180,0.35), transparent 55%),
      radial-gradient(ellipse at 20% 85%, rgba(40,40,32,0.45), transparent 50%),
      linear-gradient(160deg, var(--sepia-light) 0%, var(--sepia-mid) 55%, var(--sepia-dark) 100%);
  }
  .postcard__type {
    position: absolute;
    inset: 0;
  }
  .invite-line {
    font-family: "Bowlby One", sans-serif;
    font-size: 44px;
    fill: var(--cream);
    stroke: var(--ink);
    stroke-width: 2px;
    paint-order: stroke;
  }
  .invite-line--shadow { fill: var(--ink); stroke: none; }
  .guest-name {
    font-family: "Alfa Slab One", serif;
    font-size: 300px;
  }
  .guest-name--shadow { fill: var(--ink); }
  .guest-name--face {
    fill: var(--chili);
    stroke: var(--cream);
    stroke-width: 14px;
    paint-order: stroke;
  }
  .guest-name--inline {
    fill: none;
    stroke: var(--ink);
    stroke-width: 3px;
  }
  .birthday {
    font-family: "Yellowtail", cursive;
    font-size: 118px;
  }
  .birthday--shadow { fill: var(--ink); }
  .birthday--face {
    fill: var(--cream);
    stroke: var(--ink);
    stroke-width: 3px;
    paint-order: stroke;
  }
  .greeting-script {
    font-family: "Yellowtail", cursive;
    font-size: 44px;
    fill: var(--chili);
    stroke: var(--ink);
    stroke-width: 2px;
    paint-order: stroke;
  }
  .greeting-from {
    font-family: "Allura", cursive;
    font-size: 42px;
    fill: var(--cream);
  }
  .greeting-place {
    font-family: "Abril Fatface", serif;
    font-size: 52px;
    letter-spacing: 10px;
  }
  .greeting-place--shadow { fill: var(--ink); }
  .greeting-place--face {
    fill: var(--chili);
    stroke: var(--cream);
    stroke-width: 2px;
    paint-order: stroke;
  }
</style>
</head>
<body>
<main class="postcard">
  <div class="postcard__photo" role="img" aria-label="Faded sepia photograph of a group of people in sombreros outside a ranch building with palm fronds"></div>

  <svg class="postcard__type" width="1200" height="857" viewBox="0 0 1200 857" xmlns="http://www.w3.org/2000/svg">
    <g class="invite">
      <text class="invite-line invite-line--shadow" x="169" y="191" textLength="510" lengthAdjust="spacingAndGlyphs">YOU’RE INVITED TO...</text>
      <text class="invite-line" x="164" y="186" textLength="510" lengthAdjust="spacingAndGlyphs">YOU’RE INVITED TO...</text>
    </g>

    <g class="name">
      <text class="guest-name guest-name--shadow" x="140" y="540" textLength="930" lengthAdjust="spacingAndGlyphs">PACO’S</text>
      <text class="guest-name guest-name--face" x="115" y="518" textLength="930" lengthAdjust="spacingAndGlyphs">PACO’S</text>
    </g>

    <g class="age">
      <text class="birthday birthday--shadow" x="602" y="622">40th!</text>
      <text class="birthday birthday--face" x="594" y="614">40th!</text>
    </g>

    <g class="greeting">
      <text class="greeting-script" x="290" y="722">Greetings</text>
      <text class="greeting-from" x="476" y="720">from</text>
      <text class="greeting-place greeting-place--shadow" x="570" y="730" textLength="330" lengthAdjust="spacingAndGlyphs">MEXICO</text>
      <text class="greeting-place greeting-place--face" x="580" y="724" textLength="330" lengthAdjust="spacingAndGlyphs">MEXICO</text>
    </g>
  </svg>
</main>
</body>
</html>
```